Business Coach needs an elegant business card design

I need a business card design based around my logo for color and to look like a millionaire dollar coach. Incorporate the color of my logo with something creative and attractive that stands out. I am focused on high end companies and the card must look and feel that way.

Target Market(s)

High End Companies and Business Owners - Training People to become millionaires

Industry/Entity Type

Business

Requirements
Must have
• Front -
Logo (attached file) - Website (kolverbask.com) - Name (Darvel Kemp) Phone (412.807.5531) - Email (darvel@kolverbask.com) (My Title - Success Coach)
Back -
Slogan - Vision (see it) . Action (do it) . Transformation (be it)
Website - Learn More @ kolverbask.com

Creative High End Look!
Nice to have
Should not have
• Cheap standard look
nothing traditional

```html
<!DOCTYPE html>
<html lang="en">
<head>
<meta charset="utf-8">
<title>Darvel Kemp Coaching – Business Card</title>
<link rel="stylesheet" href="https://fonts.googleapis.com/css2?family=Open+Sans:wght@400;600;700&display=swap">
<style>
  :root {
    --navy: #13204a;
    --grey-band: #8a8c91;
    --grey-light: #c9cacd;
    --card-front: #ffffff;
    --card-back: #ebebea;
    --page: #e4e4e4;
    --text-dark: #2b2b2e;
    --ring: rgba(120, 124, 132, 0.16);
  }
  * { box-sizing: border-box; margin: 0; padding: 0; }
  html, body {
    width: 1200px; height: 675px; overflow: hidden;
    background: var(--page);
    font-family: "Open Sans", Arial, sans-serif;
  }
  .stage {
    width: 1200px; height: 675px;
    display: flex; align-items: center; justify-content: center; gap: 40px;
  }
  .card {
    position: relative; width: 525px; height: 300px; overflow: hidden;
    box-shadow: 0 6px 18px rgba(0,0,0,0.12);
  }
  .card-front { background: var(--card-front); }
  .card-back { background: var(--card-back); }
  .card-art { position: absolute; inset: 0; }

  .brand {
    position: absolute; left: 30px; top: 42px;
    display: flex; align-items: center; gap: 12px;
  }
  .brand-dot {
    width: 46px; height: 46px; border-radius: 50%; background: var(--navy);
  }
  .brand-name {
    color: var(--navy); font-weight: 600; font-size: 21px;
    line-height: 1.1; letter-spacing: 1.5px; text-transform: uppercase;
  }
  .brand-name small { display: block; font-size: 13px; letter-spacing: 5px; }

  .contact {
    position: absolute; left: 30px; top: 140px;
    list-style: none; color: var(--text-dark); font-size: 13.5px;
  }
  .contact li { display: flex; align-items: center; gap: 10px; height: 19px; }
  .contact svg { width: 13px; height: 13px; fill: var(--navy); flex: none; }

  .holder {
    position: absolute; right: 30px; top: 128px; text-align: right; color: #fff;
  }
  .holder-name { font-weight: 700; font-size: 17px; }
  .holder-title { font-size: 12.5px; opacity: 0.9; }

  .slogan {
    position: absolute; inset: 0;
    display: flex; flex-direction: column; align-items: center; justify-content: center;
    color: var(--text-dark); font-size: 15.5px; line-height: 1.45; text-align: center;
  }
  .slogan strong { color: var(--navy); font-weight: 700; }
  .learn-more { margin-top: 18px; font-size: 13px; }
</style>
</head>
<body>
<main class="stage">

  <section class="card card-front" aria-label="Card front">
    <svg class="card-art" viewBox="0 0 525 300" aria-hidden="true">
      <circle cx="420" cy="58" r="80" fill="none" stroke="var(--ring)" stroke-width="10"/>
      <path d="M525 60 C420 70 380 125 330 185 C285 240 190 255 0 250 L0 262 C200 268 300 250 345 198 C395 140 430 88 525 82 Z" fill="var(--grey-light)"/>
      <path d="M525 78 C425 86 385 138 338 196 C290 252 195 266 0 262 L0 276 C200 281 300 266 350 210 C400 152 430 102 525 96 Z" fill="var(--grey-band)"/>
      <path d="M525 96 C430 102 400 152 350 210 C300 266 200 281 0 276 L0 300 L525 300 Z" fill="var(--navy)"/>
    </svg>

    <div class="brand">
      <span class="brand-dot"></span>
      <p class="brand-name">Darvel Kemp<small>Coaching</small></p>
    </div>

    <ul class="contact">
      <li><svg viewBox="0 0 16 16"><path d="M3 1h3l1 4-2 1a9 9 0 0 0 5 5l1-2 4 1v3a2 2 0 0 1-2 2A13 13 0 0 1 1 3a2 2 0 0 1 2-2z"/></svg>412.807.5531</li>
      <li><svg viewBox="0 0 16 16"><path d="M1 3h14v10H1z M2 4l6 5 6-5" fill="var(--navy)"/><path d="M2 4.5l6 4.5 6-4.5" stroke="#fff" stroke-width="1.2" fill="none"/></svg>darvel@kolverbask.com</li>
      <li><svg viewBox="0 0 16 16"><circle cx="8" cy="8" r="7"/><path d="M1 8h14M8 1c-3 3-3 11 0 14M8 1c3 3 3 11 0 14" stroke="#fff" stroke-width="1" fill="none"/></svg>www.kolverbask.com</li>
    </ul>

    <div class="holder">
      <p class="holder-name">Darvel Kemp</p>
      <p class="holder-title">Success Coach</p>
    </div>
  </section>

  <section class="card card-back" aria-label="Card back">
    <svg class="card-art" viewBox="0 0 525 300" aria-hidden="true">
      <circle cx="262" cy="150" r="122" fill="none" stroke="var(--ring)" stroke-width="12"/>
    </svg>
    <div class="slogan">
      <p><strong>VISION.</strong> See What You Want</p>
      <p><strong>ACTION.</strong> Do What It Takes</p>
      <p><strong>TRANSFORMATION.</strong> Live Your Vision!</p>
      <p class="learn-more"><strong>Learn More:</strong> www.kolverbask.com</p>
    </div>
  </section>

</main>
</body>
</html>
```